10' x 4' outdoor vinyl banner

My company prepare and sell delicious Maryland Style Gourmet Crab Cake sandwiches at public events like fairs, festivals and concerts.
We use a 10' x 10' tent to prepare and sell this sandwiches at those events. I need a 10x4 (10 feet long by 4 feet high) banner display for the top of the tent. The same design should be scalable to another 10x3 banner for the bottom of the tent.
I need a general design of a banner with a wording that should be very attention catching
The wording is: "Maryland Crab Cake Sandwiches"
I would like also to incorporate into the design a blue crab (this is the name of specific type of crab that I'm looking for, is not just a crab painted in blue)
The theme of the design should be the sea, the shoreline, maybe some fishing boat, waves, etc, in that spirit.
I would like to use a nice blue color in the background, as we are talking about the sea and marine themes.
There are some other wordings that I would like to incorporate into the banner:
A Traditional Chesapeake Bay recipe with 100% All Natural, Blue Crab Meat . . . Rich and Flavorful . . .
This type should be in smaller size, but still visible, maybe in italics or an elegant font type.
I want something simple, inviting, like my delicious sandwiches.

```html
<!DOCTYPE html>
<html lang="en">
<head>
<meta charset="utf-8">
<title>Maryland Crab Cake Sandwiches – Tent Banner Variants</title>
<link rel="stylesheet" href="https://fonts.googleapis.com/css2?family=Archivo:wdth,wght@125,900&family=Roboto+Condensed:wght@700&display=swap">
<style>
  :root {
    --page: #ffffff;
    --divider: #111111;
    --sky: #e4f1f6;
    --sea-deep: #3f97b3;
    --sea-light: #8cc6d6;
    --surf: #dfe9ee;
    --foam: #c9dbe3;
    --sand: #c9b99b;
    --sand-dark: #a8987c;
    --crab-shell: #3f8a86;
    --crab-claw: #3f86d9;
    --panel-rim: #9fd4ee;
    --panel-edge: #3a7fcf;
    --panel-face: #f4f8fb;
    --ink-black: #121318;
    --ink-slate: #4b4d57;
    --ink-white: #f4f4f4;
    --accent-aqua: #a6d8e4;
    --flavor-blue: #2c3fc8;
    --wood-light: #e7953a;
    --wood-mid: #c8671b;
    --wood-dark: #8e3e0c;
    --wood-edge: #4f2205;
    --display: "Archivo", "Arial Black", sans-serif;
    --condensed: "Roboto Condensed", "Arial Narrow", sans-serif;
  }
  * { box-sizing: border-box; margin: 0; padding: 0; }
  html, body {
    width: 1200px; height: 978px; overflow: hidden; background: var(--page);
  }
  .sheet { position: relative; width: 1200px; height: 978px; }
  .banner {
    position: absolute; left: 12px; width: 1176px; height: 466px; overflow: hidden;
  }
  .banner--slate { top: 9px; }
  .banner--timber { top: 500px; }
  .sheet__divider {
    position: absolute; left: 12px; top: 486px; width: 1176px; height: 2px; background: var(--divider);
  }
  .banner__shore {
    position: absolute; inset: 0;
    background: linear-gradient(to bottom,
      var(--sky) 0%, var(--sea-light) 3%, var(--sea-deep) 10%, var(--sea-light) 17%,
      var(--surf) 26%, var(--foam) 50%, var(--surf) 70%, var(--sand) 80%, var(--sand-dark) 100%);
  }
  .banner__crab {
    position: absolute; top: 160px; width: 228px; height: 162px; border-radius: 50%;
    background: radial-gradient(ellipse at center, var(--crab-shell) 0%, var(--crab-shell) 38%, var(--crab-claw) 60%, rgba(63,134,217,0) 72%);
  }
  .banner__crab--left { left: 5px; }
  .banner__crab--right { left: 944px; }
  .banner__lettering { position: absolute; inset: 0; width: 1176px; height: 466px; }

  .title-panel__rim { fill: var(--panel-rim); stroke: var(--panel-edge); stroke-width: 3; }
  .title-panel__face { fill: var(--panel-face); }
  .title-word { font-family: var(--display); font-weight: 900; font-stretch: 125%; }
  .tagline { font-family: var(--condensed); font-weight: 700; font-size: 37px; fill: var(--ink-white); }
  .tagline__accent { fill: var(--accent-aqua); }
  .flavor-line { font-family: var(--display); font-weight: 900; font-stretch: 125%; font-size: 34px; fill: var(--flavor-blue); }
  .flavor-line--reflection { opacity: 0.28; }

  .banner--slate .title-box { fill: var(--ink-black); }
  .banner--slate .title-word--lead { fill: var(--ink-white); }
  .banner--slate .title-word--main { fill: var(--ink-slate); }

  .banner--timber .title-box { fill: url(#wood-grain); stroke: var(--wood-edge); stroke-width: 3; }
  .banner--timber .title-word--lead { fill: var(--ink-white); stroke: var(--wood-edge); stroke-width: 2; }
  .banner--timber .title-word--main { fill: url(#wood-grain); stroke: var(--wood-edge); stroke-width: 3; paint-order: stroke; }
</style>
</head>
<body>
<main class="sheet">

  <section class="banner banner--slate">
    <div class="banner__shore" role="img" aria-label="Photo of a sandy shoreline with breaking sea waves"></div>
    <div class="banner__crab banner__crab--left" role="img" aria-label="Blue crab illustration"></div>
    <div class="banner__crab banner__crab--right" role="img" aria-label="Blue crab illustration"></div>
    <svg class="banner__lettering" viewBox="0 0 1176 466" xmlns="http://www.w3.org/2000/svg">
      <rect class="title-panel__rim" x="200" y="28" width="776" height="384" rx="16"/>
      <rect class="title-panel__face" x="210" y="36" width="756" height="368" rx="10"/>
      <rect class="title-box" x="215" y="40" width="735" height="80"/>
      <text class="title-word title-word--lead" x="579" y="112" font-size="78" text-anchor="middle" textLength="712" lengthAdjust="spacingAndGlyphs">MARYLAND</text>
      <text class="title-word title-word--main" x="581" y="196" font-size="86" text-anchor="middle" textLength="632" lengthAdjust="spacingAndGlyphs">CRAB CAKE</text>
      <text class="title-word title-word--main" x="579" y="298" font-size="100" text-anchor="middle" textLength="712" lengthAdjust="spacingAndGlyphs">SANDWICHES</text>
      <rect class="title-box" x="217" y="309" width="723" height="93"/>
      <text class="tagline" x="578" y="350" text-anchor="middle" textLength="690" lengthAdjust="spacingAndGlyphs"><tspan class="tagline__accent">A TRADITIONAL</tspan> CHESAPEAKE BAY RECIPE</text>
      <text class="tagline" x="578" y="392" text-anchor="middle" textLength="690" lengthAdjust="spacingAndGlyphs">WITH 100% ALL NATURAL, <tspan class="tagline__accent">BLUE CRAB MEAT</tspan></text>
      <text class="flavor-line" x="587" y="436" text-anchor="middle" textLength="424" lengthAdjust="spacingAndGlyphs">RICH AND FLAVORFUL</text>
      <text class="flavor-line flavor-line--reflection" x="587" y="436" text-anchor="middle" textLength="424" lengthAdjust="spacingAndGlyphs" transform="translate(0 872) scale(1 -1)" aria-hidden="true">RICH AND FLAVORFUL</text>
    </svg>
  </section>

  <div class="sheet__divider"></div>

  <section class="banner banner--timber">
    <div class="banner__shore" role="img" aria-label="Photo of a sandy shoreline with breaking sea waves"></div>
    <div class="banner__crab banner__crab--left" role="img" aria-label="Blue crab illustration"></div>
    <div class="banner__crab banner__crab--right" role="img" aria-label="Blue crab illustration"></div>
    <svg class="banner__lettering" viewBox="0 0 1176 466" xmlns="http://www.w3.org/2000/svg">
      <defs>
        <linearGradient id="wood-grain" x1="0" y1="0" x2="0" y2="1">
          <stop offset="0" stop-color="var(--wood-light)"/>
          <stop offset="0.5" stop-color="var(--wood-mid)"/>
          <stop offset="1" stop-color="var(--wood-dark)"/>
        </linearGradient>
      </defs>
      <rect class="title-panel__rim" x="200" y="28" width="776" height="384" rx="16"/>
      <rect class="title-panel__face" x="210" y="36" width="756" height="368" rx="10"/>
      <rect class="title-box" x="215" y="40" width="735" height="80"/>
      <text class="title-word title-word--lead" x="579" y="112" font-size="78" text-anchor="middle" textLength="712" lengthAdjust="spacingAndGlyphs">MARYLAND</text>
      <text class="title-word title-word--main" x="581" y="196" font-size="86" text-anchor="middle" textLength="632" lengthAdjust="spacingAndGlyphs">CRAB CAKE</text>
      <text class="title-word title-word--main" x="579" y="298" font-size="100" text-anchor="middle" textLength="712" lengthAdjust="spacingAndGlyphs">SANDWICHES</text>
      <rect class="title-box" x="217" y="309" width="723" height="93"/>
      <text class="tagline" x="578" y="350" text-anchor="middle" textLength="690" lengthAdjust="spacingAndGlyphs"><tspan class="tagline__accent">A TRADITIONAL</tspan> CHESAPEAKE BAY RECIPE</text>
      <text class="tagline" x="578" y="392" text-anchor="middle" textLength="690" lengthAdjust="spacingAndGlyphs">WITH 100% ALL NATURAL, <tspan class="tagline__accent">BLUE CRAB MEAT</tspan></text>
      <text class="flavor-line" x="587" y="436" text-anchor="middle" textLength="424" lengthAdjust="spacingAndGlyphs">RICH AND FLAVORFUL</text>
      <text class="flavor-line flavor-line--reflection" x="587" y="436" text-anchor="middle" textLength="424" lengthAdjust="spacingAndGlyphs" transform="translate(0 872) scale(1 -1)" aria-hidden="true">RICH AND FLAVORFUL</text>
    </svg>
  </section>

</main>
</body>
</html>
```